I need a design with just the number 24. must be in blue color (royal blue) should be large enough for people see must be in the center of page. Place a nice border around the page.

Requirements
Must have
• Number 24 in Royal blue color

```html
<!DOCTYPE html>
<html lang="en">
<head>
<meta charset="utf-8">
<title>Number 24 Sign</title>
<link rel="stylesheet" href="https://fonts.googleapis.com/css2?family=Fira+Sans:wght@800&display=swap">
<style>
  :root {
    --sign-blue: #0000ff;
    --ornament-tint: #c9c9fb;
    --sign-white: #ffffff;
  }
  html, body {
    margin: 0;
    padding: 0;
    width: 1120px;
    height: 1200px;
    overflow: hidden;
    background: var(--sign-white);
  }
  .sign {
    display: block;
    width: 1120px;
    height: 1200px;
  }
  .frame-line {
    fill: none;
    stroke: var(--sign-blue);
    stroke-width: 2.2;
  }
  .ornament {
    fill: var(--ornament-tint);
  }
  .house-number {
    font-family: "Fira Sans", Arial, sans-serif;
    font-weight: 800;
    font-size: 665px;
    font-variant-numeric: oldstyle-nums;
    font-feature-settings: "onum" 1;
    letter-spacing: -0.02em;
    fill: var(--sign-blue);
  }
</style>
</head>
<body>
<svg class="sign" viewBox="0 0 1120 1200" xmlns="http://www.w3.org/2000/svg">
  <g class="border">
    <rect class="frame-line" x="41.5" y="43.5" width="1037" height="1111"/>
    <rect class="frame-line" x="51.5" y="54" width="1017" height="1091"/>
  </g>

  <g class="border-ornaments">
    <rect class="ornament" role="img" aria-label="Decorative scroll ornament, top left corner" x="28" y="25" width="82" height="84"/>
    <rect class="ornament" role="img" aria-label="Decorative scroll ornament, top right corner" x="1010" y="25" width="82" height="84"/>
    <rect class="ornament" role="img" aria-label="Decorative scroll ornament, bottom left corner" x="28" y="1091" width="82" height="84"/>
    <rect class="ornament" role="img" aria-label="Decorative scroll ornament, bottom right corner" x="1010" y="1091" width="82" height="84"/>
    <rect class="ornament" role="img" aria-label="Decorative scroll ornament, left side middle" x="32" y="562" width="30" height="74"/>
    <rect class="ornament" role="img" aria-label="Decorative scroll ornament, right side middle" x="1058" y="562" width="30" height="74"/>
  </g>

  <text class="house-number" x="558" y="708" text-anchor="middle">24</text>
</svg>
</body>
</html>
```